Flyer Design for Norvane LLC

We need a Flyer for a new company called “Norvane LLC”. This is a technology process improvement company providing a comprehensive assessment of the technology used to run their business. The documentation and review process delivers the visibility and reassurance they need to protect their business and plan for the future. The product is called “Systems Charterwork”. Our primary target is small-medium size businesses, with the deliverables going to the decision maker.

We would like to see the designs use the color blue. Our tag line is "Protect Your Business · Take Control of IT".

- Attached: Norvane LLC Overview document we put together as a starting point. Use as much or as little as you wish.
- Attached: Business Card and Logo designs for colors, etc.

Industry/Entity Type

It Company

```html
<!DOCTYPE html>
<html lang="en">
<head>
<meta charset="utf-8">
<title>Norvane LLC – Protect Your Business Flyer</title>
<link rel="stylesheet" href="https://fonts.googleapis.com/css2?family=Oswald:wght@400;500;600;700&family=Jost:wght@400;500;600&family=Arimo:wght@700&display=swap">
<style>
  :root {
    --blue: #1565c8;
    --blue-deep: #0c4fa8;
    --blue-light: #3f8ae0;
    --ink: #1c1c1c;
    --dark: #2b2b2d;
    --paper: #ffffff;
    --paper-shade: #e6e9ed;
    --stage: #d7dbe0;
  }
  * { margin: 0; padding: 0; box-sizing: border-box; }
  html, body { width: 1200px; height: 1200px; overflow: hidden; background: var(--stage); }
  .flyer {
    position: absolute; left: 170px; top: 44px; width: 860px; height: 1112px;
    background: linear-gradient(180deg, var(--paper) 0%, #f4f5f7 55%, var(--paper-shade) 100%);
    overflow: hidden; box-shadow: 0 8px 30px rgba(0,0,0,.25);
    font-family: "Jost", sans-serif; color: var(--ink);
  }
  .hero-photo { position: absolute; left: 0; top: 0; width: 600px; height: 470px; }
  .brand-band { position: absolute; left: 570px; top: 100px; width: 250px; height: 590px; background: linear-gradient(180deg, var(--blue) 0%, var(--blue-deep) 100%); }
  .logo-box {
    position: absolute; left: 582px; top: 100px; width: 226px; height: 180px; background: var(--paper);
    clip-path: polygon(0 0, 100% 0, 100% 82%, 50% 100%, 0 82%);
    display: flex; align-items: center; justify-content: center; gap: 10px; padding-bottom: 24px;
  }
  .logo-dot { width: 20px; height: 20px; border-radius: 50%; background: var(--blue); flex: none; }
  .logo-name { font-family: "Oswald", sans-serif; font-weight: 600; font-size: 32px; color: var(--blue); letter-spacing: 1px; white-space: nowrap; }
  .tagline { position: absolute; left: 570px; top: 305px; width: 250px; text-align: center; color: var(--paper); font-family: "Oswald", sans-serif; }
  .tagline-main { font-size: 62px; font-weight: 700; line-height: 1; letter-spacing: 0; white-space: nowrap; }
  .tagline-sub { font-size: 30px; font-weight: 400; line-height: 1.1; margin-top: 8px; white-space: nowrap; }
  .tagline-small { font-family: "Jost", sans-serif; font-size: 17px; font-weight: 600; letter-spacing: 1.5px; margin-top: 4px; white-space: nowrap; }
  .areas-wheel { position: absolute; left: 490px; top: 520px; width: 330px; height: 340px; }
  .areas-wheel text { font-family: "Oswald", sans-serif; }
  .intro { position: absolute; left: 60px; top: 480px; width: 440px; }
  .intro-heading {
    display: inline-block; font-family: "Arimo", sans-serif; font-size: 22px; color: var(--blue);
    padding: 9px 44px 9px 14px; background: var(--paper);
    border: 2px solid var(--ink); clip-path: polygon(0 0, 92% 0, 100% 50%, 92% 100%, 0 100%);
  }
  .intro-lead { color: var(--blue); font-size: 15px; line-height: 1.3; margin-top: 16px; }
  .intro-body { font-size: 13.5px; line-height: 1.35; margin-top: 16px; }
  .contact-card { position: absolute; left: 60px; top: 835px; width: 440px; height: 150px; }
  .contact-portrait { position: absolute; left: 0; top: 0; width: 140px; height: 140px; border: 3px solid var(--blue); background: linear-gradient(180deg, #f2f3f5, #c9ccd1); }
  .contact-details { position: absolute; left: 170px; top: 14px; }
  .contact-name { font-family: "Arimo", sans-serif; font-size: 21px; color: var(--blue); letter-spacing: .5px; }
  .contact-role { font-size: 13px; margin-top: 2px; letter-spacing: .5px; }
  .contact-line { display: flex; align-items: center; gap: 10px; font-size: 15px; margin-top: 8px; }
  .contact-line svg { width: 22px; height: 22px; }
  .contact-web { font-family: "Arimo", sans-serif; font-size: 17px; color: var(--blue); margin-top: 8px; }
  .deliverables { position: absolute; left: 520px; top: 870px; width: 300px; height: 172px; border: 2px solid var(--blue); border-radius: 14px; background: var(--paper); padding: 28px 14px 0 30px; }
  .deliverables-tab { position: absolute; left: -2px; top: -16px; background: var(--blue); color: var(--paper); font-family: "Jost", sans-serif; font-weight: 600; font-size: 17px; letter-spacing: 1px; padding: 4px 18px 4px 14px; border-radius: 16px 16px 16px 0; white-space: nowrap; }
  .deliverables ul { list-style: none; font-size: 12.5px; line-height: 1.3; }
  .deliverables li { white-space: nowrap; }
  .deliverables li::before { content: ""; display: inline-block; width: 5px; height: 5px; border-radius: 50%; background: var(--blue); margin: 0 8px 2px -13px; }
  .footer-label { position: absolute; left: 0; top: 1030px; width: 320px; height: 62px; background: var(--blue); clip-path: polygon(0 0, 84% 0, 100% 100%, 0 100%); color: var(--paper); font-family: "Oswald", sans-serif; font-size: 24px; display: flex; align-items: center; padding-left: 40px; white-space: nowrap; }
  .footer-bar { position: absolute; left: 260px; top: 1050px; width: 600px; height: 62px; background: var(--dark); clip-path: polygon(8% 0, 100% 0, 100% 100%, 0 100%); color: var(--paper); font-size: 19px; display: flex; align-items: center; padding-left: 90px; letter-spacing: .5px; white-space: nowrap; }
</style>
</head>
<body>
<div class="flyer">
  <svg class="hero-photo" viewBox="0 0 600 470" role="img" aria-label="Photo of hands reviewing printed blue charts beside a laptop keyboard">
    <defs>
      <linearGradient id="photoTone" x1="0" y1="0" x2="1" y2="1">
        <stop offset="0" stop-color="#e9eef5"/>
        <stop offset=".55" stop-color="#c7ced8"/>
        <stop offset="1" stop-color="#8d96a3"/>
      </linearGradient>
    </defs>
    <path d="M0 0 H600 V440 C520 460 470 470 430 450 C390 425 360 425 300 430 C200 440 110 400 0 350 Z" fill="url(#photoTone)"/>
    <path d="M0 350 C110 400 200 440 300 430 C360 425 390 425 430 450 C470 470 520 460 600 440" fill="none" stroke="#1565c8" stroke-width="9"/>
  </svg>

  <div class="brand-band"></div>
  <div class="logo-box"><span class="logo-dot"></span><span class="logo-name">Norvane LLC</span></div>
  <div class="tagline">
    <div class="tagline-main">PROTECT</div>
    <div class="tagline-sub">YOUR BUSINESS</div>
    <div class="tagline-small">TAKE CONTROL OF IT</div>
  </div>

  <svg class="areas-wheel" viewBox="0 0 330 340">
    <circle cx="160" cy="180" r="118" fill="none" stroke="#2b2b2d" stroke-width="30"/>
    <circle cx="160" cy="180" r="100" fill="#ffffff" stroke="#1565c8" stroke-width="4"/>
    <text x="160" y="160" text-anchor="middle" font-size="22" fill="#1565c8">EVALUATING</text>
    <text x="160" y="188" text-anchor="middle" font-size="22" fill="#1c1c1c">FIVE FUNCTIONAL</text>
    <text x="160" y="216" text-anchor="middle" font-size="22" fill="#1565c8">AREAS</text>
    <g fill="#ffffff" stroke="#1565c8" stroke-width="4">
      <circle cx="160" cy="62" r="46"/>
      <circle cx="272" cy="144" r="46"/>
      <circle cx="229" cy="276" r="46"/>
      <circle cx="91" cy="276" r="46"/>
      <circle cx="48" cy="144" r="46"/>
    </g>
    <g font-size="12" fill="#1c1c1c" text-anchor="middle">
      <text x="160" y="58">IT</text><text x="160" y="74">ADMINISTRATION</text>
      <text x="272" y="140">IT SERVICE</text><text x="272" y="156">DELIVERY</text>
      <text x="229" y="272">INFRASTRUCTURE</text><text x="229" y="288">SERVICES</text>
      <text x="91" y="272">APPLICATION</text><text x="91" y="288">SERVICES</text>
      <text x="48" y="140">IT</text><text x="48" y="156">PLANNING</text>
    </g>
  </svg>

  <section class="intro">
    <h2 class="intro-heading">You have big plans, right?</h2>
    <p class="intro-lead">Technology may help you get there, but how can you plan where you want to go without defining where you are today?</p>
    <p class="intro-body">Norvane LLC provides a comprehensive assessment of the technology used to run your business. The documentation and review process delivers the visibility and reassurance you need to protect your business.</p>
    <p class="intro-body">Our team understands that each business operates on its own unique complexities, and crafting a solution requires a custom, unbiased review. Positioning your company with the right insight is intrumental to your success and our goal as your technology partner.</p>
  </section>

  <section class="contact-card">
    <div class="contact-portrait" role="img" aria-label="Portrait of the partner"></div>
    <div class="contact-details">
      <div class="contact-name">DANIEL HARPER</div>
      <div class="contact-role">PARTNER</div>
      <div class="contact-line">
        <svg viewBox="0 0 22 22"><circle cx="11" cy="11" r="11" fill="#1565c8"/><path d="M7 6 L9 6 L10 9 L8.6 10 C9.3 11.6 10.4 12.7 12 13.4 L13 12 L16 13 L16 15 C16 15.6 15.6 16 15 16 C10.5 16 6 11.5 6 7 C6 6.4 6.4 6 7 6 Z" fill="#fff"/></svg>
        <span>(866)555-0142</span>
      </div>
      <div class="contact-line">
        <svg viewBox="0 0 22 22"><circle cx="11" cy="11" r="11" fill="#1565c8"/><rect x="5.5" y="7" width="11" height="8" fill="none" stroke="#fff" stroke-width="1.4"/><path d="M5.5 7 L11 11.5 L16.5 7" fill="none" stroke="#fff" stroke-width="1.4"/></svg>
        <span>dan@norvanellc.com</span>
      </div>
      <div class="contact-web">www.norvanellc.com</div>
    </div>
  </section>

  <section class="deliverables">
    <h3 class="deliverables-tab">DOSSIER DELIVERABLES</h3>
    <ul>
      <li>Executive Dashboard</li>
      <li>Technology Product Summary</li>
      <li>Recommended IT Policies</li>
      <li>Potential Cost Savings</li>
      <li>Technology Recommendations</li>
      <li>In-depth Questionnaire</li>
      <li>Technology Product Details</li>
      <li>Full Infrastructure Detailed Report</li>
    </ul>
  </section>

  <div class="footer-label">CONTACT INFORMATION:</div>
  <div class="footer-bar">Call: 866-410-2277 | Mail: sales@norvanellc.com</div>
</div>
</body>
</html>
```